Exclusive Sleek Crowns Invite that connects barbers

I am looking for a general invitation to join a secret club of people that shave their head. I want it the size of a business card that I can hand out to people I see on the street. I want it to feel like a special exclulisve invite to a club that only they can be apart of and want to tell their friends about.

Target Market(s)

35-60 male

Industry/Entity Type

Hair

Contact Information for Business Card

I want it to look like an invite to a secret club that only people that shave their head can be apart of... I will hand it out to people that I think fir our demographic.

Font styles to use
Serif

Colors

Designer to choose colors to be used in the design.

Requirements
Must have
• A feel of exclusivity
• website address (www.sleekcrowns.com)
• logo

```html
<!DOCTYPE html>
<html lang="en">
<head>
<meta charset="utf-8">
<title>Sleek Crowns – Invitation Card</title>
<link rel="stylesheet" href="https://fonts.googleapis.com/css2?family=Marcellus&family=Open+Sans:wght@400;700&display=swap">
<style>
  :root {
    --page: #ffffff;
    --card-dark: #000000;
    --card-light: #414143;
    --mark-ink: #050505;
    --card-text: #f2f2f2;
    --label: #4a4a4a;
  }
  * { margin: 0; padding: 0; box-sizing: border-box; }
  html, body {
    width: 1200px;
    height: 800px;
    overflow: hidden;
    background: var(--page);
  }
  .sheet {
    position: relative;
    width: 1200px;
    height: 800px;
  }
  .card {
    position: absolute;
    top: 65px;
    width: 362px;
    height: 633px;
  }
  .card--outside {
    left: 197px;
    background: linear-gradient(200deg, var(--card-light) 0%, #232325 40%, #121213 75%, var(--card-dark) 100%);
  }
  .card--inside {
    left: 660px;
    background: linear-gradient(160deg, var(--card-light) 0%, #1d1d1e 45%, #0d0d0d 80%, var(--card-dark) 100%);
  }
  .brand-mark {
    position: absolute;
    left: 0;
    right: 0;
    top: 292px;
    text-align: center;
    font-family: "Marcellus", serif;
    font-size: 26px;
    letter-spacing: 1px;
    color: var(--mark-ink);
  }
  .invite-text {
    position: absolute;
    top: 68px;
    right: 19px;
    width: 230px;
    text-align: right;
    font-family: "Marcellus", serif;
    font-size: 14px;
    line-height: 20px;
    color: var(--card-text);
  }
  .brand-small {
    position: absolute;
    left: 19px;
    top: 582px;
    font-family: "Marcellus", serif;
    font-size: 11px;
    color: var(--card-text);
  }
  .contact {
    position: absolute;
    right: 19px;
    top: 565px;
    text-align: right;
    font-family: "Marcellus", serif;
    color: var(--card-text);
  }
  .contact__phone {
    font-size: 11px;
    line-height: 18px;
  }
  .contact__web {
    font-size: 12px;
    line-height: 20px;
  }
  .contact__web strong {
    font-family: "Open Sans", sans-serif;
    font-weight: 700;
    font-size: 13px;
  }
  .side-label {
    position: absolute;
    top: 702px;
    width: 362px;
    text-align: center;
    font-family: "Open Sans", sans-serif;
    font-weight: 700;
    font-size: 19px;
    color: var(--label);
  }
  .side-label--outside { left: 197px; }
  .side-label--inside { left: 660px; }
</style>
</head>
<body>
  <main class="sheet">
    <section class="card card--outside" aria-label="Card outside">
      <div class="brand-mark">Sleek Crowns</div>
    </section>

    <section class="card card--inside" aria-label="Card inside">
      <p class="invite-text">Lorem ipsum dolor sit amet, consectetur adipiscing elit. Suspendisse quis dolor nunc. Sed sagittis rhoncus metus. Pellentesque congue elit lectus, at sodales felis condimentum sit amet.</p>
      <div class="brand-small">Sleek Crowns</div>
      <div class="contact">
        <p class="contact__phone">-phone number here-</p>
        <p class="contact__web">www.<strong>sleekcrowns</strong>.com</p>
      </div>
    </section>

    <p class="side-label side-label--outside">outside</p>
    <p class="side-label side-label--inside">inside</p>
  </main>
</body>
</html>
```